Restaurant needs a vertical banner for fried catfish

Our restaurant is looking for an eye-catching 78.75in. x 36in. vertical physical banner ad for our fried catfish. Photos for the fried catfish will be provided as a reference but we will also accept anything similar to the photo. We will be using the following as our receptacle: https://www.plankoria.example/banner-stand/retractable-banner-stands/
The design must incorporate the following flavor texts:
Fried Catfish
Always Fresh!
Made from Scratch
Hand-cut Fillets
The Best Catfish in Texas
Served with fries, hush puppies, and a 32oz fountain drink
Also available by the pound!
The final design should be creative, professional, and eye-catching for customers.
Updates
Colors
Designer to choose colors to be used in the design.
Requirements
Must have
- We are open to any and all design elements, albeit the 'flavor texts' should not overpower, but complement the fried catfish photo. 'Fried Catfish' can be used in lieu of a main title/logo.
Nice to have
- Transparent or textured backgrounds that can encompass any or all part of the banner such as a cutting board, shadows, abstract, etc to show depth are a plus.
- Use of vectors or objects such as ribbons or shapes to encapsulate the 'flavor texts' are also encouraged.

```html
<!DOCTYPE html>
<html lang="en">
<head>
<meta charset="utf-8">
<title>Fried Catfish Banner</title>
<link rel="stylesheet" href="https://fonts.googleapis.com/css2?family=Arvo:wght@400;700&display=swap">
<style>
  :root {
    --page-bg: #d6d6d8;
    --night: #1f2132;
    --plum: #3a2a38;
    --maroon: #5b343a;
    --ember: #9a4234;
    --gold: #ffcd2a;
    --mint: #e4efe2;
    --white: #ffffff;
    --red: #c41f27;
    --fry-light: #f2b53a;
    --fry-dark: #b87320;
  }
  * { margin: 0; padding: 0; box-sizing: border-box; }
  html, body {
    width: 1103px; height: 1200px; overflow: hidden;
    background: var(--page-bg);
    font-family: "Arvo", Georgia, serif;
  }
  .banner {
    position: absolute; left: 290px; top: 30px;
    width: 522px; height: 1140px; overflow: hidden;
    background:
      radial-gradient(ellipse 60% 32% at 50% 78%, var(--ember) 0%, rgba(154,66,52,0) 100%),
      linear-gradient(180deg, var(--night) 0%, var(--plum) 32%, var(--maroon) 58%, #4a2c33 82%, #2b2230 100%);
  }
  .title { position: absolute; left: 0; width: 100%; text-align: center; font-weight: 700; line-height: 1; }
  .title-fried { top: 96px; left: -6px; font-size: 98px; color: var(--gold); letter-spacing: -1px; }
  .title-catfish { top: 174px; font-size: 68px; color: var(--mint); letter-spacing: 0; }
  .burst { position: absolute; left: 412px; top: 62px; width: 60px; height: 56px; }
  .promise { position: absolute; left: 0; width: 100%; text-align: center; color: var(--white); line-height: 1; }
  .promise-lead { top: 281px; font-size: 40px; }
  .promise-line { font-size: 30px; }
  .promise-line.one { top: 321px; }
  .promise-line.two { top: 356px; }
  .bubble {
    position: absolute; border-radius: 50%; background: var(--white);
    color: var(--red); text-align: center; line-height: 1;
    display: flex; flex-direction: column; justify-content: center; align-items: center;
    box-shadow: 0 4px 14px rgba(0,0,0,0.25);
  }
  .bubble-combo { left: 130px; top: 530px; width: 190px; height: 190px; z-index: 1; align-items: flex-start; padding-left: 14px; }
  .bubble-combo .small { font-size: 13.5px; line-height: 0.98; }
  .bubble-combo .big { font-size: 47px; font-weight: 700; margin-top: 2px; }
  .bubble-best { left: 270px; top: 454px; width: 160px; height: 160px; z-index: 2; }
  .bubble-best .small { font-size: 17px; line-height: 0.98; }
  .bubble-best .big { font-size: 28px; font-weight: 700; }
  .bubble-pound { left: 284px; top: 577px; width: 160px; height: 160px; z-index: 3; }
  .bubble-pound .mid { font-size: 21px; line-height: 1; }
  .bubble-pound .big { font-size: 21px; font-weight: 700; }
  .plate-photo {
    position: absolute; left: 66px; top: 712px; width: 404px; height: 192px; z-index: 4;
    border-radius: 50%;
    background: radial-gradient(ellipse at 45% 45%, var(--fry-light) 0%, #d99a34 45%, #f4f1ea 72%, #ffffff 100%);
  }
  .foreground-fries {
    position: absolute; left: -10px; top: 850px; width: 545px; height: 300px; z-index: 5;
    background:
      radial-gradient(ellipse 28% 38% at 78% 78%, rgba(242,181,58,0.85) 0%, rgba(242,181,58,0) 100%),
      radial-gradient(ellipse 26% 20% at 22% 22%, rgba(220,150,45,0.7) 0%, rgba(220,150,45,0) 100%);
    filter: blur(4px);
  }
</style>
</head>
<body>
  <main class="banner">
    <div class="title title-fried">FRIED</div>
    <div class="title title-catfish">CATFISH</div>
    <svg class="burst" viewBox="0 0 60 56" aria-hidden="true">
      <g stroke="#ffffff" stroke-width="3.5" stroke-linecap="round" fill="none">
        <line x1="8" y1="36" x2="14" y2="6"/>
        <line x1="18" y1="42" x2="36" y2="22"/>
        <line x1="26" y1="50" x2="56" y2="42"/>
      </g>
    </svg>

    <p class="promise promise-lead">ALWAYS FRESH!</p>
    <p class="promise promise-line one">MADE FROM SCRATCH</p>
    <p class="promise promise-line two">HAND-CUT FILLETS</p>

    <div class="bubble bubble-combo">
      <span class="small">SERVED WITH FRIES,<br>HUSH PUPPIES, AND<br>A 32OZ FOUNTAIN</span>
      <span class="big">DRINK</span>
    </div>
    <div class="bubble bubble-best">
      <span class="small">THE BEST<br>CATFISH IN</span>
      <span class="big">TEXAS</span>
    </div>
    <div class="bubble bubble-pound">
      <span class="mid">ALSO<br>AVAILABLE<br>BY THE</span>
      <span class="big">POUND!</span>
    </div>

    <div class="plate-photo" role="img" aria-label="Plate of fried catfish fillets over fries with hush puppies and a cup of tartar sauce"></div>
    <div class="foreground-fries" role="img" aria-label="Blurred fried catfish pieces in the foreground"></div>
  </main>
</body>
</html>
```